Create banner ads for a digital product that deletes personal information from the web

The context of the banners is general advertisement for our service.
Please provide us with a set of static and flash/gif banners in the following standard sizes for the theme you create:
160x600
300x250
300x600
320x250
336x280
728x90
Please see our website for logo (just our name) and theme ideas - please follow similar color/font schemes if possible. www.quietlanternhub.com
Our company is an online service that deletes personal information from the internet for our members (automated opt-outs and content removal). Our target audience is anyone who wishes to protect their personal information from being on the internet (i.e. prefer to fly under the internet radar, for example). This is a product for U.S. residents who value privacy and online reputation. We seek to provide members with control of what 300+ websites are sharing about them – removing names, addresses, ages, phone numbers, email addresses, children’s information, home/property value information etc.
Industry/Entity Type
Internet
Look and feel
Each slider illustrates characteristics of the customer's brand and the style your logo design should communicate.

```html
<!DOCTYPE html>
<html lang="en">
<head>
<meta charset="utf-8">
<title>Quiet Lantern Hub – Privacy Banner 300x600</title>
<link rel="stylesheet" href="https://fonts.googleapis.com/css2?family=Arimo:ital,wght@0,400;0,700;1,700&family=Archivo+Narrow:wght@500&display=swap">
<style>
  :root {
    --paper: #ffffff;
    --ink: #111111;
    --rule: #e4e4e4;
    --box-border: #c9c9c9;
    --tab-grey: #6a6a6a;
    --tab-active: #c8264b;
    --suggest-red: #e8265a;
    --suggest-blue: #1a2fd6;
    --alarm-red: #e3261c;
    --alarm-soft: #f28b7c;
    --logo-blue: #3b6fd8;
    --band-red: #e61e14;
    --band-text: #ffffff;
  }
  html, body {
    margin: 0;
    padding: 0;
    width: 1200px;
    height: 2400px;
    overflow: hidden;
    background: var(--paper);
  }
  .banner {
    position: relative;
    width: 1200px;
    height: 2400px;
    background: var(--paper);
    font-family: "Arimo", Arial, sans-serif;
    color: var(--ink);
    overflow: hidden;
  }
  .search-header {
    position: absolute;
    left: 0; top: 0;
    width: 1200px; height: 240px;
    border-bottom: 4px solid var(--rule);
  }
  .brand-name {
    position: absolute;
    left: 8px; top: 56px;
    font-size: 104px;
    font-weight: 400;
    color: var(--logo-blue);
    letter-spacing: -4px;
    line-height: 1;
  }
  .search-box {
    position: absolute;
    left: 484px; top: 60px;
    width: 740px; height: 116px;
    border: 4px solid var(--box-border);
    box-sizing: border-box;
    padding-left: 22px;
    font-size: 64px;
    line-height: 108px;
    white-space: nowrap;
  }
  .result-tabs {
    position: absolute;
    left: 0; top: 340px;
    width: 1200px;
    font-size: 56px;
    color: var(--tab-grey);
    white-space: nowrap;
  }
  .result-tabs span { position: absolute; top: 0; }
  .tab-web { left: 532px; color: var(--tab-active); font-weight: 700; }
  .tab-images { left: 780px; }
  .tab-video { left: 1100px; }
  .tabs-rule {
    position: absolute;
    left: 0; top: 448px;
    width: 1200px; height: 4px;
    background: var(--rule);
  }
  .results {
    position: absolute;
    left: 68px; top: 626px;
    width: 1120px;
    font-size: 68px;
    line-height: 82px;
  }
  .results p { margin: 0; }
  .suggest-label { color: var(--suggest-red); }
  .suggest-query {
    color: var(--suggest-blue);
    font-weight: 700;
    font-style: italic;
    white-space: pre;
  }
  .no-results { margin-top: 68px !important; }
  .no-match { margin-top: 78px !important; }
  .no-match strong { font-weight: 700; }
  .privacy-alert {
    position: absolute;
    left: 0; top: 1784px;
    width: 1200px;
    text-align: center;
    font-family: "Archivo Narrow", "Arial Narrow", sans-serif;
    font-weight: 500;
    font-size: 124px;
    line-height: 118px;
    letter-spacing: -4px;
    color: var(--alarm-red);
    margin: 0;
  }
  .privacy-alert .soft { color: var(--alarm-soft); }
  .site-band {
    position: absolute;
    left: 0; top: 2300px;
    width: 1200px; height: 100px;
    background: var(--band-red);
  }
  .site-address {
    position: absolute;
    right: 18px; top: 0;
    font-size: 60px;
    line-height: 100px;
    color: var(--band-text);
  }
</style>
</head>
<body>
  <div class="banner">
    <header class="search-header">
      <div class="brand-name">Seekly</div>
      <div class="search-box">Uncle Sam Information</div>
    </header>

    <nav class="result-tabs">
      <span class="tab-web">Web</span>
      <span class="tab-images">Images</span>
      <span class="tab-video">Video</span>
    </nav>
    <div class="tabs-rule"></div>

    <section class="results">
      <p class="suggest-label">Did you mean:</p>
      <p class="suggest-query">Uncle Sean  Siam Information</p>
      <p class="no-results">No results containing all your search terms were found.</p>
      <p class="no-match">Your search - <strong>Uncle Sam Information</strong> - did not match any documents.</p>
    </section>

    <h1 class="privacy-alert">Your Personal <span class="soft">Privacy</span><br>is threatened daily.</h1>

    <footer class="site-band">
      <span class="site-address">www.quietlanternhub.com</span>
    </footer>
  </div>
</body>
</html>
```